Venture Capital firm needs modern business cards

We are a Venture Capital firm within financial services/Asset management. The industry generally has basic business cards with black, blue and maybe green/yellow design elements.
Our firm has a four-colour swoosh logo. We are based in London and want to stand out, just a little bit!, from the crowd. Our company is called ROLK Investments and the 'C' stands for collaboration thus using artfolkhub is a natural portal for our business card design competition. Our logo came via artfolkhub too!
We use 'Venture Partner in Asset Management' as our tagline and this is Trademark registered. We operate in a conservative industry and we should not overstep our mark. The logo is colorful as it is and therefore the rest of the design should not be too fanciful.
The objective is twofold: make our logo element stick and memorable with our audience, whilst representing a conservative yet young image.
The Business Card obviously needs a field for Name, Surname, Job Title, Adress fields: Street, City, Postcode, Country, telefone and cell number, website address, etc.
We have uploaded the ai file. We trust that these are OK. If not, please advise.
Reason: We have have been busy with a client engagement. We will set the project as Guaranteed in return for the troubles we cause. Apologies for the confusion.
Thank you all for these great and creative design suggestions. The team is very happy with a number of your ideas! We will be in touch tomorrow to give individual feedback before the project closes on Friday. We look forward to working with some of you to narrow down your creations. Thank you, ROLK Investments team.
All,
Target Market(s)
Financial Services Professionals, Investors, Media, 35-70 years, mainly male, well educated
Industry/Entity Type
Conservative
Requirements
Must have
- We must make use of our logo and potential tagline 'Venture Partner in Asset Management' as we are establishing a new Brand and new company in the market.
We can use 'ROLK', 'ROLK Investments', and 'ROLK Investments'+tagline 'Venture Partner in Asset Management' or simply the four-colour swoosh plus the name of the company as part of the text. (see files)
All design elements are available in black or grey-scale if required. (grey scale swoosh attached).
Due to regulation we must have the following wording on the card in small print 'ROLK Investments is an Appointed Representative of Brambury Monetary Ventures Limited, which is authorised by the Pemberton Oversight Board'.
Nice to have
- We would consider designs that make use of different printing techniques such embossing/debossing, UV spot etc.
We attach our colour palette in the files section for your reference.
Should not have
- The font we use for our company name is 'EXO' so do not use a font style that clashes with the corporate fonts, please.
Do not use other design elements than the ones we provide in the file library as part of this project.

```html
<!DOCTYPE html>
<html lang="en">
<head>
<meta charset="utf-8">
<title>ROLK Investments – Business Card</title>
<link rel="stylesheet" href="https://fonts.googleapis.com/css2?family=Exo+2:wght@400;600;800&family=Arimo:wght@400&display=swap">
<style>
  :root {
    --backdrop: #e9e9ea;
    --card: #fbfbfa;
    --ink: #4a4a4a;
    --ink-soft: #6d6d6d;
    --brand-green: #8cc43f;
    --icon: #7a7a7a;
    --shadow: rgba(0, 0, 0, 0.12);
  }
  * { box-sizing: border-box; margin: 0; padding: 0; }
  html, body {
    width: 1200px;
    height: 800px;
    overflow: hidden;
    background: var(--backdrop);
  }
  .canvas {
    width: 1200px;
    height: 800px;
    display: flex;
    align-items: center;
    justify-content: center;
    gap: 60px;
  }
  .card {
    width: 525px;
    height: 300px;
    background: var(--card);
    box-shadow: 0 6px 18px var(--shadow);
    position: relative;
  }
  /* Back: contact details */
  .card--back {
    display: flex;
    flex-direction: column;
    align-items: center;
    padding-top: 34px;
    font-family: "Arimo", Arial, sans-serif;
    color: var(--ink-soft);
  }
  .brand {
    display: flex;
    align-items: center;
    gap: 10px;
  }
  .brand__dot {
    width: 22px;
    height: 22px;
    border-radius: 50%;
    background: var(--ink);
  }
  .brand__name {
    font-family: "Exo 2", sans-serif;
    font-weight: 600;
    font-size: 34px;
    line-height: 1;
    color: var(--ink);
    letter-spacing: 0.5px;
  }
  .person__name {
    margin-top: 10px;
    font-family: "Exo 2", sans-serif;
    font-weight: 800;
    font-size: 24px;
    color: var(--brand-green);
    letter-spacing: -0.3px;
    line-height: 1;
  }
  .person__title {
    font-size: 13px;
    margin-top: 3px;
  }
  .contact {
    list-style: none;
    margin-top: 8px;
    display: flex;
    flex-direction: column;
    align-items: center;
    font-size: 13px;
  }
  .contact__item {
    display: flex;
    flex-direction: column;
    align-items: center;
    gap: 3px;
    margin-bottom: 5px;
  }
  .contact__icon { width: 14px; height: 14px; fill: none; stroke: var(--icon); stroke-width: 1.5; }
  .contact__icon--solid { fill: var(--icon); stroke: none; }
  .legal {
    position: absolute;
    left: 0;
    right: 0;
    bottom: 14px;
    text-align: center;
    font-size: 7px;
    color: var(--ink-soft);
  }
  /* Front: brand mark area */
  .card--front {
    display: flex;
    align-items: center;
    justify-content: center;
  }
  .card--front .brand__dot { width: 40px; height: 40px; }
  .card--front .brand__name { font-size: 64px; }
</style>
</head>
<body>
<main class="canvas">
  <section class="card card--back" aria-label="Card back with contact details">
    <div class="brand">
      <span class="brand__dot" aria-hidden="true"></span>
      <span class="brand__name">ROLK</span>
    </div>
    <h1 class="person__name">MARCUS ELLERY</h1>
    <p class="person__title">Graphic designer</p>
    <ul class="contact">
      <li class="contact__item">
        <svg class="contact__icon" viewBox="0 0 14 14" aria-hidden="true"><rect x="4" y="1" width="6" height="12" rx="1"/><line x1="6" y1="11" x2="8" y2="11"/></svg>
        <span>+44 20 7946 0183</span>
      </li>
      <li class="contact__item">
        <svg class="contact__icon" viewBox="0 0 14 14" aria-hidden="true"><rect x="1" y="3" width="12" height="8"/><polyline points="1,3 7,8 13,3"/></svg>
        <span>http://www.rolk.net</span>
      </li>
      <li class="contact__item">
        <svg class="contact__icon contact__icon--solid" viewBox="0 0 14 14" aria-hidden="true"><path d="M7 1a4 4 0 0 0-4 4c0 3 4 8 4 8s4-5 4-8a4 4 0 0 0-4-4zm0 5.5a1.5 1.5 0 1 1 0-3 1.5 1.5 0 0 1 0 3z"/></svg>
      </li>
    </ul>
    <p class="legal">ROLK Investments is an Appointed Representative of Brambury Monetary Ventures Limited, which is authorised by the Pemberton Oversight Board</p>
  </section>

  <section class="card card--front" aria-label="Card front with company name">
    <div class="brand">
      <span class="brand__dot" aria-hidden="true"></span>
      <span class="brand__name">ROLK</span>
    </div>
  </section>
</main>
</body>
</html>
```